Water ATM Card

Need a design for water ATM cards. Size of card is 3.375 x 2.125 inch
On the Front include the Cedar brook Logo.
Bottom right corner should have Price $100
On the Back
This card is to be used to access water refills at any Cedar Brook Water Vending Machines.
Please contact (869) 614 2938 or (869) 731 4072 or email clearflowhq@examplemail.com for any assistance or recharging of card.

```html
<!DOCTYPE html>
<html lang="en">
<head>
<meta charset="utf-8">
<title>Cedar Brook Water Card</title>
<link rel="stylesheet" href="https://fonts.googleapis.com/css2?family=Montserrat:wght@400;500;700&display=swap">
<style>
  :root {
    --stage: #9b9b9b;
    --card-white: #ffffff;
    --brand-blue: #2f74b8;
    --name-blue: #2a56a6;
    --icon-blue: #2d5fae;
    --ink: #1f1f1f;
    --price-green: #3a9e45;
    --back-top: #2f80c0;
    --back-mid: #3d5498;
    --back-bottom: #2b3a85;
    --on-dark: #ffffff;
  }
  * { box-sizing: border-box; margin: 0; padding: 0; }
  html, body { width: 1093px; height: 1200px; overflow: hidden; }
  body {
    background: var(--stage);
    font-family: "Montserrat", sans-serif;
    position: relative;
  }
  .card {
    position: absolute;
    left: 264px;
    width: 581px;
    height: 364px;
    border-radius: 18px;
    overflow: hidden;
  }
  .card--front { top: 225px; background: var(--card-white); }
  .card--back {
    top: 616px;
    background: linear-gradient(160deg, var(--back-top) 0%, var(--back-mid) 50%, var(--back-bottom) 100%);
    color: var(--on-dark);
  }
  .brand-name {
    position: absolute;
    left: 0;
    width: 310px;
    top: 202px;
    text-align: center;
    font-weight: 700;
    font-size: 20px;
    letter-spacing: 0.3px;
    color: var(--brand-blue);
    text-transform: uppercase;
  }
  .divider {
    position: absolute;
    left: 280px;
    top: 126px;
    width: 1.5px;
    height: 146px;
    background: var(--brand-blue);
  }
  .holder-name {
    position: absolute;
    left: 292px;
    top: 124px;
    font-weight: 700;
    font-size: 19px;
    color: var(--name-blue);
    text-transform: uppercase;
  }
  .holder-role {
    position: absolute;
    left: 292px;
    top: 151px;
    font-size: 12.5px;
    color: var(--ink);
  }
  .contacts { position: absolute; left: 292px; top: 188px; list-style: none; }
  .contacts li {
    display: flex;
    align-items: center;
    height: 22px;
    font-size: 13px;
    color: var(--ink);
  }
  .contacts li.gap { margin-top: 5px; }
  .contacts svg { width: 13px; height: 13px; margin-right: 5px; fill: var(--icon-blue); flex: none; }
  .price {
    position: absolute;
    right: 38px;
    top: 311px;
    font-weight: 700;
    font-size: 19px;
    color: var(--price-green);
  }
  .back-name {
    position: absolute;
    left: 0; right: 0;
    top: 192px;
    text-align: center;
    font-weight: 700;
    font-size: 35px;
    letter-spacing: 0.5px;
    text-transform: uppercase;
  }
  .back-note {
    position: absolute;
    left: 0; right: 0;
    top: 313px;
    text-align: center;
    font-size: 13.5px;
  }
</style>
</head>
<body>
  <section class="card card--front" aria-label="Card front">
    <div class="brand-name">Cedar Brook</div>
    <div class="divider"></div>
    <h1 class="holder-name">Dana Whitfield</h1>
    <p class="holder-role">OWER</p>
    <ul class="contacts">
      <li>
        <svg viewBox="0 0 24 24" aria-hidden="true"><path d="M6.6 10.8a15.1 15.1 0 0 0 6.6 6.6l2.2-2.2a1 1 0 0 1 1-.25 11.4 11.4 0 0 0 3.6.57 1 1 0 0 1 1 1V20a1 1 0 0 1-1 1A17 17 0 0 1 3 4a1 1 0 0 1 1-1h3.5a1 1 0 0 1 1 1c0 1.25.2 2.45.57 3.57a1 1 0 0 1-.25 1z"/></svg>
        (869) 614 2938
      </li>
      <li class="gap">
        <svg viewBox="0 0 24 24" aria-hidden="true"><path d="M7 1h10a2 2 0 0 1 2 2v18a2 2 0 0 1-2 2H7a2 2 0 0 1-2-2V3a2 2 0 0 1 2-2zm0 3v14h10V4zm5 15.5a1.2 1.2 0 1 0 0 2.4 1.2 1.2 0 0 0 0-2.4z"/></svg>
        (869) 731 4072
      </li>
      <li>
        <svg viewBox="0 0 24 24" aria-hidden="true"><path d="M2 5h20v2l-10 6L2 7zm0 4.3 10 6 10-6V19H2z"/></svg>
        clearflowhq@examplemail.com
      </li>
      <li>
        <svg viewBox="0 0 24 24" aria-hidden="true"><path d="M12 2a10 10 0 1 0 0 20 10 10 0 0 0 0-20zm-1 17.9A8 8 0 0 1 4.2 10.4L9 15v1a2 2 0 0 0 2 2zm6.9-2.5A2 2 0 0 0 16 16h-1v-3a1 1 0 0 0-1-1H8v-2h2a1 1 0 0 0 1-1V7h2a2 2 0 0 0 2-2v-.4a8 8 0 0 1 2.9 12.8z"/></svg>
        www.cedarbrookwater.example
      </li>
    </ul>
    <p class="price">Price $100</p>
  </section>

  <section class="card card--back" aria-label="Card back">
    <div class="back-name">Cedar Brook</div>
    <p class="back-note">for any assistance or recharging of card.</p>
  </section>
</body>
</html>
```